Web Header needed for an inspirational coaching company's website - ongoing work

We need a beautifully designed web header to replace my current one at my homepage on my website www.brekavol.com
There will be continuous work required for various creative work in the future if your work is selected.
I work with corporate professionals and executives to bring clarity and joy back to their career. It needs to be elegant, sophisticated, intelligent, but friendly and inspiring at the same time.
Brief and the sample header size are attached in my files
Thank you!
Target Market(s)
Corporate profesionals and executives
Industry/Entity Type
It Company
Colors
Designer to choose colors to be used in the design.
Look and feel
Each slider illustrates characteristics of the customer's brand and the style your logo design should communicate.

```html
<!DOCTYPE html>
<html lang="en">
<head>
<meta charset="UTF-8">
<title>Bring Clarity to Your Career – Header</title>
<link href="https://fonts.googleapis.com/css2?family=Source+Sans+3:wght@700&display=swap" rel="stylesheet">
<style>
  :root {
    --navy: #1f2a5c;
    --mist: #f4f2f6;
    --lilac: #8f8fc8;
    --sky: #7fb0d8;
    --peach: #f6b27a;
    --orange: #f0782a;
    --sun: #f3d24a;
    --coral: #ee5a2a;
    --portrait-dark: rgba(40, 34, 38, 0.85);
    --portrait-warm: rgba(226, 190, 178, 0.7);
    --portrait-orange: rgba(239, 106, 46, 0.9);
  }
  * { margin: 0; padding: 0; box-sizing: border-box; }
  html, body { width: 1200px; height: 539px; overflow: hidden; background: var(--mist); }

  .header {
    position: relative;
    width: 1200px;
    height: 539px;
    overflow: hidden;
    background:
      radial-gradient(ellipse 260px 320px at 40px 330px, rgba(127,176,216,0.55), transparent 70%),
      radial-gradient(ellipse 300px 260px at 260px 520px, rgba(143,143,200,0.6), transparent 70%),
      linear-gradient(90deg, #e6e4ea 0%, #f7f6f4 30%, #fbe7d2 48%, var(--peach) 58%, var(--orange) 70%, var(--orange) 100%);
  }

  .closeup-photo {
    position: absolute;
    left: 500px;
    top: 0;
    width: 700px;
    height: 539px;
    background:
      radial-gradient(ellipse 340px 240px at 560px 60px, rgba(243,210,74,0.95), transparent 70%),
      radial-gradient(ellipse 260px 160px at 520px 230px, rgba(250,228,140,0.8), transparent 75%),
      radial-gradient(ellipse 300px 220px at 620px 480px, rgba(238,90,42,0.9), transparent 70%),
      linear-gradient(90deg, rgba(240,120,42,0) 0%, rgba(240,120,42,0.55) 35%, rgba(246,160,80,0.6) 60%, rgba(243,200,90,0.5) 100%);
  }

  .portrait-photo {
    position: absolute;
    left: 0;
    top: 30px;
    width: 380px;
    height: 509px;
    background:
      radial-gradient(ellipse 170px 260px at 240px 220px, var(--portrait-warm), transparent 75%),
      linear-gradient(180deg, transparent 0%, var(--portrait-dark) 30%, var(--portrait-dark) 62%, var(--portrait-orange) 82%, var(--portrait-orange) 100%);
    -webkit-mask-image: radial-gradient(ellipse 200px 300px at 220px 320px, #000 55%, transparent 100%);
    mask-image: radial-gradient(ellipse 200px 300px at 220px 320px, #000 55%, transparent 100%);
    opacity: 0.9;
  }

  .headline {
    position: absolute;
    left: 360px;
    top: 105px;
    width: 520px;
    font-family: "Source Sans 3", "Source Sans Pro", sans-serif;
    font-weight: 700;
    font-size: 55px;
    line-height: 55px;
    letter-spacing: 2px;
    color: var(--navy);
    text-align: center;
    text-transform: uppercase;
    white-space: nowrap;
  }
  .headline span { display: block; }
</style>
</head>
<body>
  <header class="header">
    <div class="closeup-photo" role="img" aria-label="Warm orange and yellow toned close-up photograph of the coach's smile"></div>
    <div class="portrait-photo" role="img" aria-label="Portrait photograph of the smiling coach with long dark hair in an orange sleeveless top"></div>
    <h1 class="headline">
      <span>Bring clarity to</span>
      <span>your career</span>
    </h1>
  </header>
</body>
</html>
```